Label Redesign For Hemp Oil Tincture Bottle*

I need a label redesigned for Marbleleaf Hemp, current bottle label and logo is attached. The current label doesn't standout, not sure if its the font size or colors on the existing label. It is very important to have on the label that this is a Premium Full Spectrum Hemp Oil that is 2000mg. Then after the label is redesigned and approved, I would need to packaging to be designed to match the approved label design.
This Hemp oil has a relaxing effect to help ease mental and emotional stress, tension and worry. The Omega Fatty Acids it contains also naturally improves your mood and overall brain function, causing you to feel more alert and focused. Hemp Oil helps with insomnia. Take some 2-3 hours before bedtime, you will feel relaxed yet aware of how tired you are that it will lead to a good night's sleep. Hemp Oil helps ease chronic pain and inflammation from conditions such as arthritis, fibromyalgia, lupus, and MS. As a pain relief supplement, it is a safer, natural, non-chemical and non-addictive alternative to prescription painkillers.

Target Market(s)

Adults

Industry/Entity Type

Supplement

Font styles to use
Serif
Sans Serif

Colors

Designer to choose colors to be used in the design.

Requirements
Must have
• All information thats on current label but where it says 750 in the front of the existing label, it needs to say 2000. The 2000 should be prominent on the label.

```html
<!DOCTYPE html>
<html lang="en">
<head>
<meta charset="utf-8">
<title>Marbleleaf Hemp – Zero THC Premium Hemp Oil Packaging</title>
<link rel="stylesheet" href="https://fonts.googleapis.com/css2?family=Open+Sans:wght@400;600&display=swap">
<style>
  :root {
    --backdrop: #d6d6d6;
    --paper: #ffffff;
    --ink: #1d1d1b;
    --lime: #a9cd2f;
    --lime-text: #b6d536;
    --grey-mark: #8a8a8a;
  }
  html, body {
    margin: 0;
    padding: 0;
    width: 1200px;
    height: 801px;
    overflow: hidden;
    background: var(--backdrop);
  }
  .canvas {
    position: relative;
    width: 1200px;
    height: 801px;
    font-family: "Open Sans", sans-serif;
  }
  .carton-front {
    position: absolute;
    left: 375px;
    top: 120px;
    width: 232px;
    height: 558px;
  }
  .bottle-label {
    position: absolute;
    left: 656px;
    top: 424px;
    width: 148px;
    height: 232px;
  }
  .panel { display: block; width: 100%; height: 100%; overflow: hidden; }
  .panel text { font-family: "Open Sans", sans-serif; }
  .brand-name { fill: var(--grey-mark); font-weight: 600; }
  .brand-dot { fill: var(--lime); }
  .band { fill: var(--ink); }
  .claim-small { fill: var(--lime-text); font-weight: 600; }
  .claim-large { fill: var(--lime-text); font-weight: 400; }
  .detail { fill: var(--ink); font-weight: 400; }
</style>
</head>
<body>
<main class="canvas">

  <section class="carton-front" aria-label="Carton front panel">
    <svg class="panel" viewBox="0 0 290 698" xmlns="http://www.w3.org/2000/svg">
      <rect width="290" height="698" fill="var(--paper)"/>
      <rect x="0" y="420" width="290" height="278" fill="var(--lime)"/>
      <circle class="brand-dot" cx="145" cy="150" r="10"/>
      <text class="brand-name" x="145" y="205" font-size="26" text-anchor="middle">Marbleleaf Hemp</text>
      <g transform="rotate(-9 145 420)">
        <rect class="band" x="40" y="346" width="178" height="50" rx="6"/>
        <rect class="band" x="-40" y="392" width="380" height="110"/>
        <text class="claim-small" x="50" y="380" font-size="30">ZERO THC</text>
        <text class="claim-large" x="8" y="436" font-size="58">PREMIUM</text>
        <text class="claim-large" x="42" y="464" font-size="26">FULL SPECTRUM</text>
        <text class="claim-large" x="62" y="492" font-size="26">2000 HEMP OIL</text>
      </g>
      <text class="detail" x="145" y="530" font-size="13" text-anchor="middle">2000 mg</text>
      <text class="detail" x="145" y="549" font-size="13" text-anchor="middle">Dietary Suppement</text>
      <text class="detail" x="145" y="588" font-size="13" text-anchor="middle">Natural Peppermint Flavor</text>
    </svg>
  </section>

  <section class="bottle-label" aria-label="Bottle label">
    <svg class="panel" viewBox="0 0 185 290" xmlns="http://www.w3.org/2000/svg">
      <rect width="185" height="290" fill="var(--paper)"/>
      <rect x="0" y="170" width="185" height="120" fill="var(--lime)"/>
      <circle class="brand-dot" cx="92" cy="28" r="6"/>
      <text class="brand-name" x="92" y="62" font-size="15" text-anchor="middle">Marbleleaf Hemp</text>
      <g transform="rotate(-9 92 170)">
        <rect class="band" x="25" y="114" width="124" height="36" rx="4"/>
        <rect class="band" x="-30" y="146" width="245" height="73"/>
        <text class="claim-small" x="32" y="138" font-size="21">ZERO THC</text>
        <text class="claim-large" x="2" y="176" font-size="39">PREMIUM</text>
        <text class="claim-large" x="26" y="195" font-size="17">FULL SPECTRUM</text>
        <text class="claim-large" x="38" y="213" font-size="17">2000 HEMP OIL</text>
      </g>
      <text class="detail" x="92" y="241" font-size="9" text-anchor="middle">2000 mg</text>
      <text class="detail" x="92" y="254" font-size="9" text-anchor="middle">Dietary Suppement</text>
      <text class="detail" x="92" y="280" font-size="9" text-anchor="middle">Natural Peppermint Flavor</text>
    </svg>
  </section>

</main>
</body>
</html>
```